Lantern Holdings Business Card

We are looking to design new business cards for our company. We have two office locations and would like to have both full addresses on the card. Each address needs two lines for the building name and street address and a line or two for the city, state and zip code. There should be a place for 2-3 phone numbers. The addresses and phone numbers are at the bottom of this description. We also need a place to put our company website and one email address. Our logo is attached.
We would like the card to be two sided. The back of the card should have a blue background with some part of our logo design on it. We would like the full logo on the front of the card as well. The front of the card should have a white background with the blue logo. We are open to listing our addresses on the front or the back of the card. The person who designed our logo gave us an excellent business card idea that we really liked. I have attached a picture of his business card idea so that we can build off of it.
Addresses:
The Marlow Exchange
2214 47th Street NW
Washington, DC 20419
Osprey Harbor Tower
815 Tamsin Boulevard #2207
Miami, FL 33987
Phone Numbers: (202) 555-0148
(202) 555-0193
Website: www.lanternholdings-example.com

```html
<!DOCTYPE html>
<html lang="en">
<head>
<meta charset="utf-8">
<title>Lantern Holdings Business Card</title>
<link rel="stylesheet" href="https://fonts.googleapis.com/css2?family=Lato:wght@400&display=swap">
<style>
  :root {
    --page: #ffffff;
    --board-center: #f7f7f8;
    --board-edge: #d6d7d9;
    --navy: #2a3578;
    --white: #ffffff;
    --shadow: rgba(0, 0, 0, 0.35);
  }
  * { margin: 0; padding: 0; box-sizing: border-box; }
  html, body {
    width: 1200px;
    height: 969px;
    overflow: hidden;
    background: var(--page);
  }
  .board {
    position: absolute;
    left: 24px;
    top: 24px;
    width: 1152px;
    height: 921px;
    background: radial-gradient(ellipse 55% 55% at 50% 50%, var(--board-center) 0%, var(--board-center) 30%, var(--board-edge) 100%);
  }
  .card {
    position: absolute;
    left: 371px;
    width: 410px;
    height: 234px;
    border-radius: 16px;
    overflow: hidden;
    box-shadow: 0 3px 7px var(--shadow);
    font-family: "Lato", sans-serif;
  }
  .card-front {
    top: 185px;
    background: var(--white);
  }
  .card-back {
    top: 502px;
    background: var(--navy);
  }
  .brand {
    position: absolute;
    right: 22px;
    top: 97px;
    display: flex;
    align-items: center;
    gap: 8px;
    color: var(--navy);
  }
  .brand-mark {
    width: 24px;
    height: 24px;
    background: var(--navy);
    border-radius: 3px;
  }
  .brand-name {
    font-size: 23px;
    letter-spacing: 0.5px;
    text-transform: uppercase;
    line-height: 1;
  }
  .web-line {
    position: absolute;
    left: 22px;
    right: 22px;
    top: 201px;
    display: flex;
    justify-content: space-between;
    font-size: 10.5px;
    color: var(--navy);
  }
  .contact {
    position: absolute;
    left: 23px;
    color: var(--white);
    font-size: 12px;
    line-height: 16px;
  }
  .office-dc { top: 21px; }
  .phones { top: 98px; }
  .phones p + p { margin-top: 4px; }
  .office-miami { top: 167px; }
  .emblem-panel {
    position: absolute;
    left: 216px;
    top: 0;
    right: 0;
    bottom: 0;
    background: var(--white);
    border-radius: 20px 0 0 20px;
  }
</style>
</head>
<body>
  <div class="board">
    <section class="card card-front" aria-label="Card front">
      <div class="brand">
        <span class="brand-mark"></span>
        <span class="brand-name">Lantern Holdings</span>
      </div>
      <div class="web-line">
        <span class="website">www.lanternholdings-example.com</span>
        <span class="email">info@lanternholdings-example.com</span>
      </div>
    </section>

    <section class="card card-back" aria-label="Card back">
      <address class="contact office-dc">
        The Marlow Exchange<br>
        2214 47th Street NW<br>
        Washington, DC 20419
      </address>
      <div class="contact phones">
        <p>(202) 555-0148</p>
        <p>(202) 555-0193</p>
      </div>
      <address class="contact office-miami">
        Osprey Harbor Tower<br>
        815 Tamsin Boulevard #2207<br>
        Miami, FL 33987
      </address>
      <div class="emblem-panel"></div>
    </section>
  </div>
</body>
</html>
```